Updating our Raw Materials Brochure

Please update and modify (to add more space for the additional text) the brochure designed for us in January (see attached file) so we can circulate a May 2021 version. Thanks and hope your family is OK despite the terrible tragedy going on with Covid-19 in India. Best wishes!

```html
<!DOCTYPE html>
<html lang="en">
<head>
<meta charset="utf-8">
<title>Raw Materials May 2021 Market Update</title>
<link rel="stylesheet" href="https://fonts.googleapis.com/css2?family=Cinzel:wght@400;600;700&family=EB+Garamond:wght@500;600&family=Lato:wght@400;700&display=swap">
<style>
  :root {
    --backdrop: #8c8c8c;
    --paper: #ffffff;
    --brand-red: #b3161c;
    --ink: #1b1b1b;
    --body-ink: #2a2a2a;
    --box-grey: #d6d6d6;
    --rule-grey: #9a9a9a;
    --chart-blue: #2e6cc0;
    --chart-orange: #e6752b;
    --chart-magenta: #e0339a;
    --chart-cyan: #25b6e6;
    --highlight: #e8e28a;
    --frame-blue: #8fb0d6;
  }
  * { box-sizing: border-box; margin: 0; padding: 0; }
  html, body { width: 1200px; height: 900px; overflow: hidden; }
  body {
    background: var(--backdrop);
    font-family: "Lato", sans-serif;
    color: var(--body-ink);
    display: flex;
    gap: 10px;
    padding: 40px 15px;
  }
  .page {
    position: relative;
    width: 580px;
    height: 820px;
    background: var(--paper);
    overflow: hidden;
  }
  .page > * { position: absolute; }

  .brand-name {
    font-family: "Cinzel", serif;
    font-weight: 700;
    color: var(--ink);
    letter-spacing: 0.5px;
  }
  .body-copy {
    font-size: 8.2px;
    line-height: 1.3;
    text-align: justify;
  }
  .body-copy p + p { margin-top: 1px; }

  /* Front page */
  .hero-photo {
    left: 0; top: 0; width: 580px; height: 262px;
    background: linear-gradient(120deg, #cfcac4 0%, #f1efec 35%, #b9b3ab 62%, #e8e5e1 85%, #a9a39b 100%);
  }
  .front .brand-name { right: 40px; top: 54px; font-size: 24px; }
  .title-band {
    left: 0; width: 580px; height: 40px;
    display: flex; align-items: center; justify-content: center;
    font-family: "Cinzel", serif; color: #fff; white-space: nowrap;
    font-size: 15px; letter-spacing: 0.5px;
  }
  .title-band strong { font-size: 23px; font-weight: 600; margin: 0 6px; }
  .front .title-band { top: 270px; background: var(--brand-red); }

  .section-tab {
    left: 0; top: 322px; width: 276px; height: 30px;
    background: var(--ink); color: #fff;
    font-family: "Cinzel", serif; font-size: 19px;
    display: flex; align-items: center; padding-left: 12px;
  }
  .shortages-copy { left: 18px; top: 362px; width: 262px; }
  .cpi-chart { left: 14px; top: 640px; width: 272px; }

  .constraints-heading {
    left: 300px; top: 324px; width: 262px;
    font-family: "Cinzel", serif; font-weight: 700; font-size: 21px;
    color: var(--brand-red); text-align: center;
    border-bottom: 1.5px solid var(--ink); padding-bottom: 3px;
  }
  .constraints-sub { left: 300px; top: 361px; font-size: 8.4px; }
  .ethylene-copy { left: 300px; top: 384px; width: 262px; }
  .ethylene-chart { left: 300px; top: 452px; width: 262px; }
  .vam-heading {
    left: 300px; top: 616px; width: 262px;
    font-family: "EB Garamond", serif; font-weight: 600; font-size: 13.5px; line-height: 1.2;
    border-bottom: 1.5px solid var(--brand-red); padding-bottom: 8px;
  }
  .vam-copy { left: 300px; top: 672px; width: 262px; }

  .footer-accent { left: 300px; top: 775px; width: 280px; height: 13px; background: var(--brand-red); }
  .footer-bar {
    left: 0; bottom: 0; width: 580px; height: 30px; background: var(--ink);
    color: #fff; font-size: 9px; letter-spacing: 5px;
    display: flex; align-items: center; justify-content: center;
  }

  /* Inside page */
  .inside .brand-name { left: 0; width: 580px; top: 52px; text-align: center; font-size: 24px; }
  .inside .title-band { top: 104px; background: var(--ink); }
  .logistics-heading {
    left: 16px; top: 150px; width: 548px; height: 42px;
    border-top: 2px dotted var(--ink); border-bottom: 2px dotted var(--ink);
    font-family: "Cinzel", serif; font-weight: 700; font-size: 19px;
    color: var(--brand-red); display: flex; align-items: center; justify-content: center;
  }
  .grey-note {
    background: var(--box-grey); padding: 10px 12px;
    font-size: 8.4px; line-height: 1.3; text-align: justify;
  }
  .demand-note { left: 16px; top: 206px; width: 270px; }
  .nightmare-chart { left: 300px; top: 202px; width: 264px; }
  .transport-chart { left: 16px; top: 312px; width: 200px; }
  .capacity-note { left: 228px; top: 350px; width: 336px; }
  .inside .resin-band {
    left: 0; top: 478px; width: 580px; height: 34px; background: var(--brand-red);
    color: #fff; font-family: "EB Garamond", serif; font-weight: 600; font-size: 17px;
    display: flex; align-items: center; justify-content: center;
  }
  .resin-chart { left: 16px; top: 526px; width: 170px; }
  .refining-copy { left: 200px; top: 526px; width: 364px; font-size: 8.4px; }
  .rubber-chart { left: 200px; top: 640px; width: 350px; }
  .inside .footer-bar { height: 26px; }
</style>
</head>
<body>

<section class="page front">
  <div class="hero-photo" role="img" aria-label="Photo of business colleagues shaking hands around a table in a bright office"></div>
  <div class="brand-name">Norvale Supply</div>
  <div class="title-band">Raw Materials <strong>MAY 2021</strong> Market Update</div>

  <h2 class="section-tab">GLOBAL SHORTAGES</h2>
  <div class="shortages-copy body-copy">
    <p>As the recovery builds momentum more manufacturers are trying to buy extra material to prevent running out. Nearly all inputs are affected and there seems to be no end in sight as supply is unable to keep up with demand.</p>
    <p>The situation has been complicated by a growing list of disasters. Starting with the deep freeze and blackouts wiping out energy and petrochemicals operations in February, the Suez canal back up in March then hackers bringing down the largest US pipeline this month.</p>
    <p>US GDP increased at a 10.7% annual rate or $554.2 billion in current dollars (adjusted to 6.4% for inflation) in the first quarter. Demand seems to be driven by personal income growing $2.4 trillion (up 59%) from increased government social benefits and pandemic relief programs. Expectations are it will continue as personal savings were $4.12 trillion (up 83% the fourth quarter) driving personal savings to 21%.</p>
    <p>The trailing 12-month Producer Price Index and Consumer Price Index were up 6.2% and 4.2% respectively. These should go higher as the trailing 4-months averages are 10.2% and 6.3% respectively. Our procurement team is focused on leveraging our global supply position and growing demand so we will continue to deliver you the most competitive costs available despite these conditions.</p>
  </div>

  <svg class="cpi-chart" viewBox="0 0 272 128" font-family="Lato, sans-serif">
    <text x="2" y="6" font-size="4.6" font-weight="700" fill="#222">Chart 2. 12-month percent change in CPI for All Urban Consumers, not seasonally adjusted, Apr. 2020 - Apr. 2021</text>
    <text x="2" y="12" font-size="4.4" fill="#444">Percent change</text>
    <rect x="22" y="16" width="240" height="92" fill="none" stroke="#bbb" stroke-width="0.6"/>
    <g font-size="4.6" fill="#444" text-anchor="end">
      <text x="18" y="110">0</text><text x="18" y="92">1</text><text x="18" y="73">2</text>
      <text x="18" y="55">3</text><text x="18" y="36">4</text><text x="18" y="18">5</text>
    </g>
    <polyline fill="none" stroke="#5a5ad8" stroke-width="1" points="28,102 47,106 66,97 85,89 104,84 123,82 142,86 161,86 180,82 199,82 218,77 237,60 256,29"/>
    <polyline fill="none" stroke="#9a3050" stroke-width="1" points="28,82 47,86 66,86 85,79 104,77 123,77 142,79 161,79 180,82 199,84 218,84 237,79 256,53"/>
    <g fill="#5a5ad8"><circle cx="28" cy="102" r="1.1"/><circle cx="47" cy="106" r="1.1"/><circle cx="66" cy="97" r="1.1"/><circle cx="85" cy="89" r="1.1"/><circle cx="104" cy="84" r="1.1"/><circle cx="123" cy="82" r="1.1"/><circle cx="142" cy="86" r="1.1"/><circle cx="161" cy="86" r="1.1"/><circle cx="180" cy="82" r="1.1"/><circle cx="199" cy="82" r="1.1"/><circle cx="218" cy="77" r="1.1"/><circle cx="237" cy="60" r="1.1"/><circle cx="256" cy="29" r="1.1"/></g>
    <g fill="#9a3050"><circle cx="28" cy="82" r="1.1"/><circle cx="47" cy="86" r="1.1"/><circle cx="66" cy="86" r="1.1"/><circle cx="85" cy="79" r="1.1"/><circle cx="104" cy="77" r="1.1"/><circle cx="123" cy="77" r="1.1"/><circle cx="142" cy="79" r="1.1"/><circle cx="161" cy="79" r="1.1"/><circle cx="180" cy="82" r="1.1"/><circle cx="199" cy="84" r="1.1"/><circle cx="218" cy="84" r="1.1"/><circle cx="237" cy="79" r="1.1"/><circle cx="256" cy="53" r="1.1"/></g>
    <g font-size="4.4" fill="#444" text-anchor="middle">
      <text x="28" y="115">Apr'20</text><text x="47" y="115">May</text><text x="66" y="115">Jun</text><text x="85" y="115">Jul</text><text x="104" y="115">Aug</text><text x="123" y="115">Sep</text><text x="142" y="115">Oct</text><text x="161" y="115">Nov</text><text x="180" y="115">Dec</text><text x="199" y="115">Jan</text><text x="218" y="115">Feb</text><text x="237" y="115">Mar</text><text x="256" y="115">Apr'21</text>
    </g>
    <rect x="60" y="119" width="150" height="8" fill="none" stroke="#bbb" stroke-width="0.5"/>
    <line x1="66" y1="123" x2="80" y2="123" stroke="#5a5ad8"/><text x="84" y="125" font-size="4.4" fill="#444">All items</text>
    <line x1="132" y1="123" x2="146" y2="123" stroke="#9a3050"/><text x="150" y="125" font-size="4.4" fill="#444">All items less food and energy</text>
  </svg>

  <h2 class="constraints-heading">KEY CONSTRAINTS</h2>
  <p class="constraints-sub">Ethylene Shortage Drives Prices Higher</p>
  <div class="ethylene-copy body-copy">
    <p>Contractual prices for Ethylene (key feedstock for water based and hot melt adhesives) increased 56% from 2020 to a 7-year high of $0.47/lb in March as multiple severe weather cracker outages driven by the deep freeze in February forced 70% capacity offline. Restarting production has been difficult as so many sites were damaged simultaneously.</p>
  </div>

  <svg class="ethylene-chart" viewBox="0 0 262 156" font-family="Lato, sans-serif">
    <text x="131" y="8" font-size="6" fill="#444" text-anchor="middle">Ethylene, Contract and Spot Pricing</text>
    <g font-size="4.4" fill="#555" text-anchor="end">
      <text x="36" y="19">$0.650</text><text x="36" y="29">$0.600</text><text x="36" y="39">$0.550</text><text x="36" y="49">$0.500</text><text x="36" y="59">$0.450</text><text x="36" y="69">$0.400</text><text x="36" y="79">$0.350</text><text x="36" y="89">$0.300</text><text x="36" y="99">$0.250</text><text x="36" y="109">$0.200</text><text x="36" y="119">$0.150</text><text x="36" y="129">$0.100</text><text x="36" y="139">$0.050</text>
    </g>
    <line x1="40" y1="137" x2="250" y2="137" stroke="#bbb" stroke-width="0.5"/>
    <polyline fill="none" stroke="var(--chart-blue)" stroke-width="1.2" points="50,87 86,88 122,85 158,74 194,74 230,61"/>
    <polyline fill="none" stroke="var(--chart-orange)" stroke-width="1.2" points="50,100 86,102 122,96 158,75 194,75 230,53"/>
    <g font-size="4.6" fill="#555" text-anchor="middle">
      <text x="50" y="144">Oct-20</text><text x="86" y="144">Nov-20</text><text x="122" y="144">Dec-20</text><text x="158" y="144">Jan-21</text><text x="194" y="144">Feb-21</text><text x="230" y="144">Mar-21</text>
    </g>
    <line x1="60" y1="150" x2="72" y2="150" stroke="var(--chart-blue)" stroke-width="1.2"/><text x="75" y="151.5" font-size="4.2" fill="#555">Meridian Index Contract NA Ethylene</text>
    <line x1="160" y1="150" x2="172" y2="150" stroke="var(--chart-orange)" stroke-width="1.2"/><text x="175" y="151.5" font-size="4.2" fill="#555">Meridian Index Spot C2</text>
  </svg>

  <h3 class="vam-heading">Vinyl Acetate Monomer (VAM) – Key Ingredient for Water Based Adhesives</h3>
  <div class="vam-copy body-copy">
    <p>VAM shortages became severe following the February winter storm driving prices up 128% since Jan-2021. All three US suppliers (Kestrel Chemical, Arbor Polymers and Halden Petrochem) declared force majeure and all four production sites were shut down. They were stuck in varying stages of restarting and ramping up to full rates for nearly 3 months so supplies remain limited and that is expected to continue through Q2 with demand currently outstripping supply.</p>
  </div>

  <div class="footer-accent"></div>
  <footer class="footer-bar">www.norvalesupply.com</footer>
</section>

<section class="page inside">
  <div class="brand-name">Norvale Supply</div>
  <div class="title-band">Raw Materials <strong>MAY 2021</strong> Market Update</div>
  <h2 class="logistics-heading">LOGISTICS LIMITATIONS VS. DEMAND GROWTH</h2>

  <p class="grey-note demand-note">The ramp up in production of consumer and industrial goods while consumers still rely more on at home delivery or pick up from stores (which require more trucks and warehousing) has created unprecedented logistics tightness.</p>

  <svg class="nightmare-chart" viewBox="0 0 264 120" font-family="Lato, sans-serif">
    <text x="4" y="8" font-size="6.4" font-weight="700" fill="#222">A Logistical Nightmare</text>
    <text x="4" y="15" font-size="4.8" fill="#444">Transport, storage and inventory costs are near record highs in the U.S.</text>
    <line x1="4" y1="21" x2="14" y2="21" stroke="#111"/><text x="16" y="22.5" font-size="4.2" fill="#444">Transportation</text>
    <line x1="52" y1="21" x2="62" y2="21" stroke="var(--chart-magenta)"/><text x="64" y="22.5" font-size="4.2" fill="#444">Warehousing</text>
    <line x1="98" y1="21" x2="108" y2="21" stroke="var(--chart-cyan)"/><text x="110" y="22.5" font-size="4.2" fill="#444">Inventories</text>
    <text x="24" y="38" font-size="4.4" fill="#444">Expansion</text>
    <text x="110" y="96" font-size="4.4" fill="#444">Contraction</text>
    <line x1="6" y1="78" x2="244" y2="78" stroke="#e0c020" stroke-width="0.8" stroke-dasharray="3 2"/>
    <polyline fill="none" stroke="#111" stroke-width="0.9" points="6,32 14,44 22,40 30,54 40,58 50,62 60,70 70,72 80,68 90,74 100,70 110,78 120,76 130,92 140,78 150,84 160,80 170,82 180,74 190,78 200,70 210,72 220,64 232,66 244,62"/>
    <polyline fill="none" stroke="var(--chart-magenta)" stroke-width="0.9" points="6,40 16,46 26,50 36,52 46,56 56,60 66,62 76,64 86,68 96,70 106,74 116,76 126,80 136,84 146,82 156,86 166,84 176,80 186,82 196,78 206,80 216,74 226,76 236,72 244,70"/>
    <polyline fill="none" stroke="var(--chart-cyan)" stroke-width="0.9" points="6,44 16,50 26,54 36,58 46,62 56,64 66,66 76,70 86,72 96,76 106,78 116,80 126,84 136,86 146,88 156,84 166,86 176,82 186,84 196,80 206,82 216,78 226,80 236,76 244,74"/>
    <g font-size="4.4" fill="#444"><text x="248" y="46">100</text><text x="248" y="64">75</text><text x="248" y="80">50</text><text x="248" y="98">25</text></g>
    <g font-size="4.4" fill="#444" text-anchor="middle"><text x="30" y="106">2019</text><text x="120" y="106">2020</text><text x="220" y="106">2021</text></g>
    <text x="4" y="114" font-size="3.8" fill="#666">Source: Freight Conditions Survey; a reading above 50 indicates expansion</text>
  </svg>

  <svg class="transport-chart" viewBox="0 0 200 150" font-family="Lato, sans-serif">
    <text x="26" y="8" font-size="5.4" font-weight="700" fill="#222">Transportation Prices</text>
    <g fill="var(--chart-blue)">
      <rect x="6" y="54" width="7" height="82"/><rect x="16" y="50" width="7" height="86"/><rect x="26" y="44" width="7" height="92"/><rect x="36" y="40" width="7" height="96"/><rect x="46" y="36" width="7" height="100"/><rect x="56" y="32" width="7" height="104"/><rect x="66" y="30" width="7" height="106"/><rect x="76" y="28" width="7" height="108"/><rect x="86" y="27" width="7" height="109"/><rect x="96" y="26" width="7" height="110"/><rect x="106" y="26" width="7" height="110"/><rect x="116" y="27" width="7" height="109"/><rect x="126" y="26" width="7" height="110"/><rect x="136" y="25" width="7" height="111"/>
    </g>
    <polyline fill="none" stroke="var(--brand-red)" stroke-width="1.2" points="6,52 26,42 46,34 66,29 86,25 106,23 126,23 146,26"/>
    <line x1="2" y1="136" x2="150" y2="136" stroke="#999" stroke-width="0.6"/>
    <text x="6" y="146" font-size="4.4" fill="#555">Apr 2020 – Apr 2021, monthly index</text>
  </svg>

  <p class="grey-note capacity-note">Capacity is constrained by slowed construction in vehicles (chips and other materials shortages) as traditional channels are idled (shopping malls, etc.). Spot Van rates were up 58.1% versus April 2020 as outages cause chain reactions. Currently there is a traffic jam of 771 barges accumulated on the lower Mississippi due to a fractured bridge, so expectations are this will continue until year end.</p>

  <h2 class="resin-band">Polyethylene and Polyurethane Prices near record highs</h2>

  <svg class="resin-chart" viewBox="0 0 170 104">
    <g stroke="#ccc" stroke-width="0.6"><line x1="4" y1="14" x2="166" y2="14"/><line x1="4" y1="38" x2="166" y2="38"/><line x1="4" y1="62" x2="166" y2="62"/><line x1="4" y1="86" x2="166" y2="86"/></g>
    <polyline fill="none" stroke="var(--brand-red)" stroke-width="1.2" points="6,84 40,80 70,74 100,66 130,44 160,20"/>
  </svg>

  <div class="refining-copy body-copy">
    <p>About 42% of US oil refining capacity went offline in February (~5.5m barrels/day) but it has recovered to over 86% by last week. The shortages this created downstream continue to create spot outages of critical inputs resulting in reduced operating rates at our suppliers.</p>
    <p>For example, Polyethylene polymers (critical in hot melt adhesives) increased 39% this year plus Benzene increased 10% in April and Polyether Polyols (key feedstock for polyurethanes) are on 75% sales allocation because of limited domestic materials and difficulty bringing in imports from marine transport shortages. As a result, the price index for rubbers and plastics is up 9% since January and is still rising.</p>
  </div>

  <svg class="rubber-chart" viewBox="0 0 350 130" font-family="Lato, sans-serif">
    <rect x="1" y="1" width="348" height="128" fill="#eef3f9" stroke="var(--frame-blue)" stroke-width="2"/>
    <text x="10" y="12" font-size="5" font-weight="700" fill="#334">Producer Price Index by Commodity: Rubber and Plastic Products</text>
    <rect x="20" y="18" width="318" height="90" fill="#fff" stroke="#bbb" stroke-width="0.5"/>
    <rect x="262" y="18" width="58" height="90" fill="var(--highlight)"/>
    <g stroke="#ddd" stroke-width="0.5"><line x1="20" y1="38" x2="338" y2="38"/><line x1="20" y1="58" x2="338" y2="58"/><line x1="20" y1="78" x2="338" y2="78"/><line x1="20" y1="98" x2="338" y2="98"/></g>
    <polyline fill="none" stroke="#1d3f8a" stroke-width="1.3" points="22,46 36,50 50,42 64,46 80,48 96,46 112,44 128,46 144,44 160,42 176,44 192,46 208,52 224,60 240,70 256,80 272,86 288,84 304,80 320,66 330,54"/>
    <g font-size="4.2" fill="#555" text-anchor="middle"><text x="40" y="116">2015</text><text x="100" y="116">2016</text><text x="160" y="116">2017</text><text x="220" y="116">2018</text><text x="280" y="116">2020</text><text x="326" y="116">2021</text></g>
    <text x="20" y="124" font-size="3.8" fill="#666">Source: U.S. Bureau of Labor Statistics</text>
  </svg>

  <footer class="footer-bar">www.norvalesupply.com</footer>
</section>

</body>
</html>
```